Skincare Cleanser Bottle Label

New product launch of a mint facial cleanser.
Brand is called Dorvella.
Product will be called Lumora.
Looking for a label design that can be printed using silk screening.
High gloss white plastic bottle. 8oz. White push pump top.
Clinical skincare brand, professional image, sold in medical spas.

Target Market(s)

Women Age 20-65

Industry/Entity Type

Health And Wellness

Font styles to use
Serif
Sans Serif

Requirements
Must have
• Dorvella brand name in the orignal font.
Should not have
• Multiple colours.

```html
<!DOCTYPE html>
<html lang="en">
<head>
<meta charset="utf-8">
<title>Dorvella Lumora Mint Facial Cleanser Label</title>
<link rel="stylesheet" href="https://fonts.googleapis.com/css2?family=Courier+Prime&display=swap">
<style>
  :root {
    --label-white: #ffffff;
    --ink: #1f1f1f;
    --band-green: #5fb12e;
    --band-green-deep: #4b9426;
    --leaf-lime: #b5dd2a;
    --leaf-lime-mid: rgba(181, 221, 42, 0.55);
    --leaf-lime-soft: rgba(181, 221, 42, 0.22);
    --type: "Courier Prime", "Courier New", monospace;
  }
  html, body {
    margin: 0;
    padding: 0;
    width: 1200px;
    height: 2542px;
    overflow: hidden;
    background: var(--label-white);
  }
  .label {
    position: relative;
    width: 1200px;
    height: 2542px;
    background: var(--label-white);
    overflow: hidden;
  }
  .leaf-artwork {
    position: absolute;
    left: 345px;
    top: 350px;
    width: 820px;
    height: 2030px;
    border-radius: 44% 52% 40% 56% / 22% 26% 24% 30%;
    background:
      radial-gradient(ellipse 60% 22% at 62% 17%, var(--leaf-lime-mid) 0%, var(--leaf-lime-soft) 70%, rgba(181,221,42,0) 100%),
      radial-gradient(ellipse 70% 24% at 48% 45%, var(--leaf-lime-mid) 0%, var(--leaf-lime-soft) 70%, rgba(181,221,42,0) 100%),
      radial-gradient(ellipse 55% 24% at 58% 78%, var(--leaf-lime-mid) 0%, var(--leaf-lime-soft) 70%, rgba(181,221,42,0) 100%),
      linear-gradient(180deg, var(--leaf-lime-soft) 0%, rgba(181,221,42,0.12) 100%);
  }
  .brand-name {
    position: absolute;
    left: 78px;
    top: 377px;
    height: 1014px;
    width: 170px;
    margin: 0;
    writing-mode: vertical-rl;
    transform: rotate(180deg);
    font-family: var(--type);
    font-weight: 400;
    font-size: 200px;
    line-height: 170px;
    text-align: center;
    text-transform: lowercase;
    color: var(--ink);
    letter-spacing: -0.04em;
  }
  .product-band {
    position: absolute;
    left: 0;
    top: 1482px;
    width: 1200px;
    height: 455px;
    background: linear-gradient(90deg, var(--band-green) 0%, var(--band-green-deep) 100%);
    opacity: 0.93;
    display: flex;
    align-items: center;
    justify-content: center;
  }
  .product-name {
    margin: 0;
    font-family: var(--type);
    font-weight: 400;
    font-size: 300px;
    line-height: 1;
    text-transform: lowercase;
    color: var(--label-white);
    letter-spacing: -0.02em;
  }
</style>
</head>
<body>
  <main class="label">
    <div class="leaf-artwork" role="img" aria-label="Outlined lime-green mint leaves stacked down the right side, marking the mint facial cleanser"></div>
    <h1 class="brand-name">Dorvella</h1>
    <section class="product-band">
      <h2 class="product-name">Lumora</h2>
    </section>
  </main>
</body>
</html>
```